Zielgruppe
Herstellung und Vertrieb von Baustoffen als Eigenmarke
Aufgabenstellung
Wiedererkennungswert unserer Marke. Technisches Verständniss für die Umsetrzung. Klares Design. Logo muss mit eingebaut werden. Rundes etikett mit Durchmesser 18 cm.

```html
<!DOCTYPE html>
<html lang="de">
<head>
<meta charset="utf-8">
<title>Bitumen Dichtband – Rundetikett</title>
<link href="https://fonts.googleapis.com/css2?family=Arimo:wght@400;700&family=Open+Sans:wght@700&display=swap" rel="stylesheet">
<style>
  :root{
    --bg:#ffffff;
    --label:#9bbccd;
    --label-dark:#8badc1;
    --band:#e84e0f;
    --band-soft:#e9694f;
    --band-alu:#e04b3c;
    --ink:#2e2e2e;
    --ink-band:#2a1a14;
    --white:#ffffff;
    --roll:#18191b;
    --roll-light:#45484c;
    --flag-black:#000000;
    --flag-red:#dd0000;
    --flag-gold:#ffce00;
  }
  html,body{margin:0;padding:0;width:1200px;height:1089px;overflow:hidden;background:var(--bg);}
  .canvas{display:block;width:1200px;height:1089px;}
  .label-disc{fill:var(--label);}
  .label-disc--alu{fill:var(--label-dark);}
  .band{fill:var(--band);}
  .band--alu{fill:var(--band-alu);}
  .t{font-family:"Arimo",Arial,sans-serif;fill:var(--ink);}
  .t-kicker{font-size:22px;font-weight:700;}
  .t-title{font-size:55px;font-weight:700;}
  .t-band-head{font-size:11px;font-weight:700;fill:var(--ink-band);}
  .t-band{font-size:10px;fill:var(--ink-band);}
  .t-heading{font-size:9.6px;font-weight:700;}
  .t-body{font-size:7.6px;}
  .t-spec{font-size:9.4px;font-weight:700;}
  .t-company{font-size:12.4px;font-weight:700;}
  .t-address{font-size:8.6px;font-weight:700;}
  .brand-box{fill:var(--white);}
  .brand-name{font-family:"Arimo",Arial,sans-serif;font-weight:700;font-size:9px;fill:var(--ink);}
  .roll-body,.roll-tail{fill:url(#rollTone);stroke:url(#rollTone);stroke-width:6;stroke-linejoin:round;}
  .badge-text{font-family:"Open Sans",Arial,sans-serif;font-weight:700;font-size:13px;text-anchor:middle;}
  .badge-text--light{fill:var(--white);}
  .badge-text--dark{fill:var(--flag-black);}
</style>
</head>
<body>
<svg class="canvas" viewBox="0 0 1200 1089" xmlns="http://www.w3.org/2000/svg">
  <defs>
    <clipPath id="discClip"><circle cx="603" cy="311" r="215"/></clipPath>
    <linearGradient id="rollTone" x1="0" y1="0" x2="1" y2="1">
      <stop offset="0" stop-color="var(--roll-light)"/>
      <stop offset="1" stop-color="var(--roll)"/>
    </linearGradient>

    <g id="labelDichtband">
      <circle class="label-disc" cx="603" cy="311" r="215"/>
      <g clip-path="url(#discClip)">
        <rect class="band" x="380" y="217" width="450" height="72"/>
        <rect class="band" x="380" y="438" width="450" height="13"/>
      </g>
      <text class="t t-kicker" x="603" y="138" text-anchor="middle">Bitumen</text>
      <text class="t t-title" x="603" y="203" text-anchor="middle">Dichtband</text>
      <text class="t t-band-head" x="603" y="233" text-anchor="middle">Dichtband zum wasserdichten Verkleben und Abdichten von</text>
      <text class="t t-band" text-anchor="middle">
        <tspan x="603" y="250">Fugen und Rissen, Regenrinnen, Anschlüssen an Dach und Wand, Abdeckungen,</tspan>
        <tspan x="603" y="264">Glasdächern und Gewächshäusern, Stahlkonstruktionen, Dacheindeckungen,</tspan>
        <tspan x="603" y="278">Trauf- und Kehlblechen.</tspan>
      </text>
      <text class="t t-heading" x="436" y="307">Verarbeitung</text>
      <text class="t t-body">
        <tspan x="436" y="321">Die zu dichtenden Oberflächen müssen trocken,</tspan>
        <tspan x="436" dy="9.1">frost-, fett- und silikonfrei sowie ab riebfest sein.</tspan>
        <tspan x="436" dy="9.1">Poröser oder staubiger Untergrund sollte mit Vor-</tspan>
        <tspan x="436" dy="9.1">anstrich (ca. 200ml/m2) vorbehandelt werden, um</tspan>
        <tspan x="436" dy="9.1">eine optimale Haftung zu erzielen. Das Bitumen</tspan>
        <tspan x="436" dy="9.1">Alu Dichtband muss nach dem Aufbringen fest an-</tspan>
        <tspan x="436" dy="9.1">gedrückt werden. Das Entstehen von Hohlstellen</tspan>
        <tspan x="436" dy="9.1">(Blasen) ist zu vermeiden. Sind mehrere</tspan>
        <tspan x="436" dy="9.1">Streifen an zusetzen muss die Überlap-</tspan>
        <tspan x="436" dy="9.1">pung mind. 50 mm betragen. Begehbare-</tspan>
        <tspan x="436" dy="9.1">bzw. befahrbare Untergründe sind zur</tspan>
        <tspan x="436" dy="9.1">Verarbeitung nicht geeignet.</tspan>
      </text>
      <text class="t t-heading" x="617" y="307">Technische Angaben</text>
      <text class="t t-body">
        <tspan x="617" y="321">Beschichtung aus Elastomerbitumen mit</tspan>
        <tspan x="617" dy="9.1">Alukaschierung.</tspan>
        <tspan x="617" dy="9.1">Verarbeitungstemperatur liegt zwischen 5° bis 45° C</tspan>
        <tspan x="617" dy="9.1">Bitumen Alu Dichtband ist ein selbstklebendes und</tspan>
        <tspan x="617" dy="9.1">kalt zu verarbeitendes Abdich tungsband. Oberflä-</tspan>
        <tspan x="617" dy="9.1">chenvergütet, UV-beständig und hat eine gute</tspan>
        <tspan x="617" dy="9.1">mechanische Standfestigkeit. Besteht aus einem</tspan>
        <tspan x="639" dy="9.1">hochwertigen Kunststoff-Harz-Bitumen-</tspan>
        <tspan x="639" dy="9.1">Gemisch, welches durch eine silikonbe-</tspan>
        <tspan x="639" dy="9.1">schichtete Folie geschützt wird.</tspan>
      </text>
      <text class="t t-spec">
        <tspan x="639" y="419">Rolle 10 m Dicke 1,5 mm</tspan>
        <tspan x="639" y="431">Made in Germany</tspan>
      </text>
      <rect class="brand-box" x="579" y="383" width="52" height="67"/>
      <text class="brand-name" x="605" y="420" text-anchor="middle">Halvorn</text>
      <text class="t t-company" x="603" y="471" text-anchor="middle">Halvorn Dämmstoffe GmbH&amp;Co.KG</text>
      <text class="t t-address" text-anchor="middle">
        <tspan x="603" y="484">Lindenweg 9  74800 Talbach</tspan>
        <tspan x="603" y="494">Telefon 06200-48215</tspan>
        <tspan x="603" y="504">kormatex@postfach.de</tspan>
      </text>
    </g>

    <g id="tapeRoll">
      <path class="roll-tail" d="M228 944 L420 872 L470 892 L306 984 Z"/>
      <rect class="roll-body" x="402" y="702" width="188" height="200" rx="46" ry="46"/>
    </g>
  </defs>

  <!-- Hauptetikett -->
  <use href="#labelDichtband"/>

  <!-- Dichtband mit Rolle -->
  <g transform="translate(-148 571.6) scale(0.67)" style="--band:var(--band-soft)">
    <use href="#labelDichtband"/>
  </g>
  <g class="tape-roll" role="img" aria-label="Foto einer schwarzen Bitumen-Dichtbandrolle mit abgewickeltem Bandende">
    <use href="#tapeRoll"/>
  </g>
  <g class="made-in-badge">
    <rect x="458" y="906" width="115" height="23" fill="var(--flag-black)"/>
    <rect x="458" y="929" width="115" height="23" fill="var(--flag-red)"/>
    <rect x="458" y="952" width="115" height="23" fill="var(--flag-gold)"/>
    <text class="badge-text badge-text--light" x="515.5" y="922.5">Hergestellt</text>
    <text class="badge-text badge-text--light" x="515.5" y="945.5">in</text>
    <text class="badge-text badge-text--dark" x="515.5" y="968.5">Deutschland</text>
  </g>

  <!-- Aluband mit Rolle -->
  <g transform="translate(376 568.6) scale(0.67)">
    <circle class="label-disc label-disc--alu" cx="603" cy="311" r="215"/>
    <g clip-path="url(#discClip)">
      <rect class="band band--alu" x="380" y="226" width="450" height="66"/>
      <rect class="band band--alu" x="380" y="438" width="450" height="9"/>
    </g>
    <text class="t t-kicker" x="603" y="138" text-anchor="middle">Bitumen</text>
    <text class="t t-title" x="603" y="206" text-anchor="middle" style="font-size:62px">Aluband</text>
    <text class="t t-band-head" x="603" y="243" text-anchor="middle" style="font-size:10.5px">Reparaturband zum wasserdichten Verkleben und Abdichten von</text>
    <text class="t t-band" text-anchor="middle" style="font-size:9.6px">
      <tspan x="603" y="257">Fugen und Rissen in Regenrinnen, Blechen, Dacheindeckungen, Glasdächern,</tspan>
      <tspan x="603" y="271">Gewächshäusern, Fahrzeugen, Caravan, Dachfenstern, Kaminen, Holzfaserplatten,</tspan>
      <tspan x="603" y="285">Faserzement Wellplatten, Mauerscheiben, Anschlüsse von Wand und Dach</tspan>
    </text>
    <text class="t t-heading" x="430" y="310">Verarbeitung</text>
    <text class="t t-body">
      <tspan x="430" y="324">Die zu verklebenden Flächen müssen frost-,</tspan>
      <tspan x="430" dy="10.4">staub- und silikonfrei sein.</tspan>
      <tspan x="430" dy="10.4">Das Band ist selbstklebend ab + 10 °C.</tspan>
      <tspan x="430" dy="10.4">Darunter kann die Beschichtung erwärmt</tspan>
      <tspan x="430" dy="10.4">oder mit Benzin aktiviert werden.</tspan>
      <tspan x="430" dy="10.4">Zur Verklebung auf Stein und porösen</tspan>
      <tspan x="430" dy="10.4">mineralischen Untergründen muss</tspan>
      <tspan x="430" dy="10.4">unser Universal Haftgrund</tspan>
      <tspan x="430" dy="10.4">vorgestrichen werden.</tspan>
    </text>
    <text class="t t-heading" x="613" y="310">Technische Daten</text>
    <text class="t t-body">
      <tspan x="613" y="324">Beschichtung aus Elastomerbitumen mit</tspan>
      <tspan x="613" dy="10.4">Alukaschierung</tspan>
      <tspan x="613" dy="10.4">Verarbeitungstemperatur + 10° bis + 40 °C</tspan>
      <tspan x="613" dy="10.4">Temperaturbeständig − 30° bis + 80 °C</tspan>
      <tspan x="613" dy="10.4">Dauerelastisch und alterungsbeständig</tspan>
      <tspan x="613" dy="10.4">Dicke 1,5 mm</tspan>
      <tspan x="636" dy="10.4">Kühl und trocken lagern</tspan>
      <tspan x="636" dy="10.4">Breite und Farbe siehe</tspan>
      <tspan x="636" dy="10.4">Seitenetikett</tspan>
    </text>
    <text class="t t-spec" x="460" y="432">Rolle 10 m Dicke 1,5 mm</text>
    <text class="t t-spec" x="636" y="432">Made in Germany</text>
    <rect class="brand-box" x="579" y="387" width="52" height="60"/>
    <text class="brand-name" x="605" y="420" text-anchor="middle">Halvorn</text>
    <text class="t t-company" x="603" y="467" text-anchor="middle">Halvorn Dämmstoffe GmbH&amp;Co.KG</text>
    <text class="t t-address" text-anchor="middle">
      <tspan x="603" y="480">Lindenweg 9   74800 Talbach</tspan>
      <tspan x="603" y="490">Telefon  06200-48215</tspan>
      <tspan x="603" y="500">kormatex@postfach.de</tspan>
    </text>
  </g>
  <g class="tape-roll" role="img" aria-label="Foto einer schwarzen Bitumen-Aluband-Rolle mit abgewickeltem Bandende" transform="translate(514 0)">
    <use href="#tapeRoll"/>
  </g>
  <g class="made-in-badge">
    <rect x="972" y="906" width="115" height="23" fill="var(--flag-black)"/>
    <rect x="972" y="929" width="115" height="23" fill="var(--flag-red)"/>
    <rect x="972" y="952" width="115" height="23" fill="var(--flag-gold)"/>
    <text class="badge-text badge-text--light" x="1029.5" y="922.5">Hergestellt</text>
    <text class="badge-text badge-text--light" x="1029.5" y="945.5">in</text>
    <text class="badge-text badge-text--dark" x="1029.5" y="968.5">Deutschland</text>
  </g>
</svg>
</body>
</html>
```